Bold, Modern, Clean "Vernatouchmassage.com" website

Why we stand out?
We are a male and female mobile massage team. Our names are Jonah and Tessa. 
Verna Touch is a Seattle based mobile massage service. Our massage is offered to the community with a goal of facilitating balance within each individual. We specialize in integrated Pain management, and sports/medical massage therapy. Every client's first assessment is attended by our male and female massage therapist team. Depending on the goals identified for an individual determines which therapist will be assigned to provide treatment, if not both.

Our passion...
Here at Verna Touch, we have a great passion for Postural Resoration and how it is integrated into an individual's Massage treatment. We pride ourselves in being natural facilitators of healing, which takes the ego of the therapist out of the client's healing process. We strive to deliver the best massage possible by including modalities such as Neuromuscular, Myofascial release, spontaneous muscle release, postural restoration, orthopedic, and medical massage.

Our education...

We are both Graduates of Alvenra, school of massage therapy. We have continuing education in medical massage, myofacial release, trigger point therapy, postural restoration, anatomy, and spontaneous muscle release. Tessa is also a Certified Yoga Instructor, which amplifies her experience with flexibility and strength as it pertains to each individual. Jonah's passion is Massage, stretching, and strength training to encourage postural restoration and realignment.

Our rates-

Our rates are $75/ 60 minutes, $95/ 90 minutes, and $120/ 120 minutes.

Education-
Both Tessa and I worked as behavioral health professionals that specialized in life skills mentoring for youth who had experienced different types of trauma. This led us both to want to help others in a different environment, where individuals can be empowered to take responsibility over their own healing. To us, massage is a type of manipulation physical therapy, that encourages healing on many levels.

Advice to any massage client-
The most important thing to 'us', as Licenced providers is to get you on to our table to show you our skills. But a good therapist never forgets that it's not about what we do for you, but what we can facilitate for you. Your health and healing has nothing to do with us. It is yours, not ours. Identify what your goals are with any Therapist, and know what the end looks like. Progress should be tangible, such as range of motion, and decreased pain.

5/5 stars Massage Therapy
Verified Review

Tessa and Jonah at Verna Touch are awesome! I recently had open heart surgery, and Tessa worked on me to increase my range of motion while helping with the pinched nerve from my arm being in the same position for so long during my surgery. My wife drives a lot for work, and Jonah has helped decrease her neck and lower back pain immensely. They are seriously the best therapists I have ever worked with. I would recommend them to anyone who needs anything from stress relief to a medical massage treatment. They are professional, up beat, easy going, and always on time. And, I love that they meet us where ever we like! We did a staycation recently, where they came to our hotel to give us relaxation massages. Although usually they come to our home, where we focus on pain related issues. We will continue to work with them for a long, long time.

Brisa K. on December 17, 2015

Target Market(s)

Mobile massage therapy clients

Industry/Entity Type

Massage Therapy

Coding

Coded - Design and coding required

Number of Pages Required

1 page

Font styles to use
Serif
Sans Serif

Requirements
Must have
• Please add or remove any information that would help the presentation of our website. Our logo is posted below, please include into the website.
• Please include a contact field that includes, vernatouchmassage@quillmail.test,
• (206) 555-0147
• We have also included our own stock photos, as well as a photo of Jonah and Tessa. Please include a cropped photo of both massage therapists.

```html
<!DOCTYPE html>
<html lang="en">
<head>
<meta charset="utf-8">
<title>Verna Touch Mobile Massage</title>
<link rel="stylesheet" href="https://fonts.googleapis.com/css2?family=Open+Sans:wght@400;600;700&family=Roboto:wght@300;400&display=swap">
<style>
:root{
  --navy:#26236b;
  --navy-deep:#1f1d5c;
  --ink:#2b2a78;
  --cyan:#15a9c9;
  --text:#333;
  --white:#fff;
  --footer:#2d2a74;
  --footer-strip:#3a3784;
}
*{margin:0;padding:0;box-sizing:border-box}
html,body{width:1200px;height:1200px;overflow:hidden}
body{position:relative;background:var(--white);font-family:'Roboto',Arial,sans-serif;color:var(--text)}
.abs{position:absolute}

/* top band */
.top-band{left:0;top:0;width:1200px;height:98px;background:linear-gradient(180deg,#2a2775,#2f2c80)}
.btn-outline{position:absolute;top:22px;width:80px;height:30px;border:1.5px solid var(--white);color:var(--white);font:400 9px 'Open Sans',sans-serif;display:flex;align-items:center;justify-content:center}
.band-shadow{left:240px;top:98px;width:720px;height:30px;background:radial-gradient(ellipse at 50% 0%,rgba(0,0,0,.22),rgba(0,0,0,0) 70%)}

/* expert zone */
.section-title{left:0;top:138px;width:1200px;text-align:center;font:400 18px 'Open Sans',sans-serif;color:var(--ink)}
.section-title b{font-weight:700}
.title-rule{left:475px;top:171px;width:250px;height:1px;background:#d8d8e2}
.title-accent{left:566px;top:170px;width:68px;height:2px;background:var(--cyan)}

.post{position:absolute;width:360px;height:90px}
.post-thumb{position:absolute;left:0;top:0;width:93px;height:86px;border:1.5px solid #aaa}
.post-body{position:absolute;left:101px;top:4px;width:256px}
.post-date{font:400 7.5px 'Roboto',sans-serif;color:var(--cyan)}
.post-title{margin-top:4px;font:600 10.2px/12.4px 'Open Sans',sans-serif;color:var(--ink)}
.post-text{margin-top:4px;font:300 8.3px/12.4px 'Roboto',sans-serif;color:#222}

.blog-btn{left:520px;top:522px;width:160px;height:31px;border:1.5px solid var(--cyan);background:var(--white);color:var(--cyan);font:600 9.6px 'Open Sans',sans-serif;display:flex;align-items:center;justify-content:center;z-index:2;letter-spacing:.2px}

/* feature band */
.feature-band{left:0;top:538px;width:1200px;height:356px;background:linear-gradient(100deg,#b8265f 0%,#8a2a6e 35%,#6a2a6a 60%,#6b2456 80%,#4a2040 100%)}
.card{position:absolute;top:597px;height:253px;border:1.5px solid var(--white)}
.video-card{left:232px;width:361px}
.video-photo{position:absolute;left:2px;top:2px;width:169px;height:248px;background:linear-gradient(160deg,#6f6f5a,#8a7360 50%,#5d5f66)}
.video-panel{position:absolute;left:171px;top:2px;width:187px;height:248px;background:var(--navy)}
.play{position:absolute;left:69px;top:108px}
.video-title{position:absolute;left:13px;top:20px;font:600 19px/19.5px 'Open Sans',sans-serif;color:var(--cyan)}
.video-lead{position:absolute;left:13px;top:68px;width:170px;font:700 10.4px/12.2px 'Open Sans',sans-serif;color:var(--white)}
.video-text{position:absolute;left:13px;top:126px;width:165px;font:400 8.3px/12.4px 'Roboto',sans-serif;color:var(--white)}
.video-btn{position:absolute;left:13px;top:202px;width:162px;height:31px;border:1.5px solid var(--cyan);color:var(--cyan);font:400 9px 'Open Sans',sans-serif;display:flex;align-items:center;justify-content:center}

.news-card{left:606px;width:362px}
.news-photo{position:absolute;left:2px;top:2px;width:355px;height:246px;background:linear-gradient(180deg,#3a1a3a 0%,#5a3a44 35%,#c7a982 70%,#d9b88c 100%)}
.news-text{position:absolute;left:0;top:22px;width:358px;text-align:center;font:400 13.4px/17.6px 'Open Sans',sans-serif;color:var(--white)}
.news-text b{font-weight:600}
.news-btn{position:absolute;left:128px;top:76px;width:105px;height:30px;border:1.5px solid var(--white);color:var(--white);font:600 9.6px 'Open Sans',sans-serif;display:flex;align-items:center;justify-content:center}

/* footer */
.footer{left:0;top:894px;width:1200px;height:306px;background:linear-gradient(90deg,#2a2870,#2e2b78 50%,#3b3783)}
.footer-strip{left:0;top:1126px;width:1200px;height:74px;background:linear-gradient(180deg,#2c2a74,#4a4690)}
.f-head{position:absolute;top:936px;font:400 12.5px 'Open Sans',sans-serif;color:var(--white)}
.f-head b{font-weight:600}
.f-rule{position:absolute;top:966px;height:1px;background:rgba(255,255,255,.18)}
.f-accent{position:absolute;top:965px;height:2px;background:var(--cyan)}
.brand-mark{left:238px;top:999px;width:80px;height:80px;border-radius:50%;background:var(--navy-deep);border:2px solid var(--white);display:flex;align-items:center;justify-content:center;text-align:center;font:600 13px/14px 'Open Sans',sans-serif;color:var(--white)}
.about-text{left:341px;top:992px;width:230px;font:300 8.3px/12.6px 'Roboto',sans-serif;color:var(--white)}
.f-links{left:600px;top:992px;list-style:none}
.f-links li{font:400 9px/17px 'Open Sans',sans-serif;color:var(--white);padding-left:9px;position:relative}
.f-links li::before{content:"›";position:absolute;left:0;color:var(--cyan);font-size:11px}
.contact{left:734px;top:990px;width:240px}
.contact-row{height:21px;display:flex;align-items:center;gap:8px;font:400 9px 'Open Sans',sans-serif;color:var(--white)}
.contact-row svg{width:10px;height:10px;flex:none}
.social{position:absolute;top:1105px;width:37px;height:37px;border-radius:50%;background:var(--cyan)}
.copyright{left:0;top:1163px;width:1200px;text-align:center;font:400 9.6px 'Open Sans',sans-serif;color:var(--white)}
</style>
</head>
<body>

<div class="abs top-band">
  <div class="btn-outline" style="left:324px">READ MORE</div>
  <div class="btn-outline" style="left:559px">READ MORE</div>
  <div class="btn-outline" style="left:794px">READ MORE</div>
</div>
<div class="abs band-shadow"></div>

<h2 class="abs section-title">The <b>Expert</b> Zone</h2>
<div class="abs title-rule"></div>
<div class="abs title-accent"></div>

<!-- posts -->
<article class="post" style="left:234px;top:207px">
  <div class="post-thumb" role="img" aria-label="Man relaxing during a head massage" style="background:linear-gradient(135deg,#e9d6c8,#b58c74 60%,#e8e1da)"></div>
  <div class="post-body"><div class="post-date">June 16th, 2015</div><div class="post-title">Lorem ipsum dolor sit amet, consectetur adipisicing elit, sed do eiusmod tempor incididunt ut labore.</div><div class="post-text">Lorem ipsum dolor sit amet, consectetur adipisicing elit, sed do eiusmod tempor incididunt ut labore et dolore magna aliqua. Ut enim ad minim veniam.</div></div>
</article>
<article class="post" style="left:610px;top:207px">
  <div class="post-thumb" role="img" aria-label="Woman doing a yoga pose by the sea" style="background:linear-gradient(180deg,#d9dde0,#c9c2b4 55%,#8f8472)"></div>
  <div class="post-body"><div class="post-date">June 16th, 2015</div><div class="post-title">Lorem ipsum dolor sit amet, consectetur adipisicing elit, sed do eiusmod tempor incididunt ut labore.</div><div class="post-text">Lorem ipsum dolor sit amet, consectetur adipisicing elit, sed do eiusmod tempor incididunt ut labore et dolore magna aliqua. Ut enim ad minim veniam.</div></div>
</article>
<article class="post" style="left:234px;top:306px">
  <div class="post-thumb" role="img" aria-label="Meditation hands on green background" style="background:linear-gradient(135deg,#4f8f3a,#7fb24c 50%,#3f6e2a)"></div>
  <div class="post-body"><div class="post-date">June 16th, 2015</div><div class="post-title">Lorem ipsum dolor sit amet, consectetur adipisicing elit, sed do eiusmod tempor incididunt ut labore.</div><div class="post-text">Lorem ipsum dolor sit amet, consectetur adipisicing elit, sed do eiusmod tempor incididunt ut labore et dolore magna aliqua. Ut enim ad minim veniam.</div></div>
</article>
<article class="post" style="left:610px;top:306px">
  <div class="post-thumb" role="img" aria-label="Facial massage treatment" style="background:linear-gradient(135deg,#f0c9a4,#d99b6e 55%,#f3dcc6)"></div>
  <div class="post-body"><div class="post-date">June 16th, 2015</div><div class="post-title">Lorem ipsum dolor sit amet, consectetur adipisicing elit, sed do eiusmod tempor incididunt ut labore.</div><div class="post-text">Lorem ipsum dolor sit amet, consectetur adipisicing elit, sed do eiusmod tempor incididunt ut labore et dolore magna aliqua. Ut enim ad minim veniam.</div></div>
</article>
<article class="post" style="left:234px;top:406px">
  <div class="post-thumb" role="img" aria-label="Candles, stones, oil and lavender" style="background:linear-gradient(135deg,#c9b9d6,#8c6fa8 45%,#3b3236)"></div>
  <div class="post-body"><div class="post-date">June 16th, 2015</div><div class="post-title">Lorem ipsum dolor sit amet, consectetur adipisicing elit, sed do eiusmod tempor incididunt ut labore.</div><div class="post-text">Lorem ipsum dolor sit amet, consectetur adipisicing elit, sed do eiusmod tempor incididunt ut labore et dolore magna aliqua. Ut enim ad minim veniam.</div></div>
</article>
<article class="post" style="left:610px;top:406px">
  <div class="post-thumb" role="img" aria-label="Woman receiving a relaxing treatment" style="background:linear-gradient(135deg,#5a3422,#b07a5c 55%,#e6c6b0)"></div>
  <div class="post-body"><div class="post-date">June 16th, 2015</div><div class="post-title">Lorem ipsum dolor sit amet, consectetur adipisicing elit, sed do eiusmod tempor incididunt ut labore.</div><div class="post-text">Lorem ipsum dolor sit amet, consectetur adipisicing elit, sed do eiusmod tempor incididunt ut labore et dolore magna aliqua. Ut enim ad minim veniam.</div></div>
</article>

<div class="abs blog-btn">VIEW OUR EXPERT’S BLOG</div>

<!-- feature band -->
<div class="abs feature-band" role="img" aria-label="Spa still life with towels, flower, incense and bowl in magenta tones"></div>

<div class="card video-card">
  <div class="video-photo" role="img" aria-label="Therapist speaking to camera in a video"></div>
  <svg class="play" width="36" height="36" viewBox="0 0 36 36" aria-hidden="true"><circle cx="18" cy="18" r="18" fill="#15a9c9"/><path d="M14 11.5 L25 18 L14 24.5 Z" fill="#fff"/></svg>
  <div class="video-panel">
    <div class="video-title">Stillwater’s<br>Video Tour</div>
    <div class="video-lead">Lorem ipsum dolor sit amet, consectetur adipisicing elit, sed do eiusmod tempor incididunt ut labore.</div>
    <div class="video-text">Ut enim ad minim veniam, quis nostrud exercitation ullamco laboris nisi ut aliquip ex ea commodo consequat. Duis aute irure dolor in reprehenderit in voluptate velit esse cillum dolore.</div>
    <div class="video-btn">VIEW ALL VIDEOS</div>
  </div>
</div>

<div class="card news-card">
  <div class="news-photo" role="img" aria-label="Treatment room with two massage tables"></div>
  <div class="news-text">Sign up for <b>Stillwater's monthly e-newsletter</b><br>to receive advanced notice of <b>special offers</b>,<br>forthcoming events and latest news.</div>
  <div class="news-btn">SUBSCRIBE NOW</div>
</div>

<!-- footer -->
<div class="abs footer"></div>
<div class="abs footer-strip"></div>

<h3 class="f-head" style="left:234px">About <b>Verna Touch Mobile Massage</b></h3>
<div class="f-rule" style="left:234px;width:332px"></div>
<div class="f-accent" style="left:234px;width:50px"></div>

<h3 class="f-head" style="left:602px">Infomation</h3>
<div class="f-rule" style="left:602px;width:113px"></div>
<div class="f-accent" style="left:602px;width:50px"></div>

<h3 class="f-head" style="left:735px">Contact Us</h3>
<div class="f-rule" style="left:735px;width:232px"></div>
<div class="f-accent" style="left:735px;width:50px"></div>

<div class="abs brand-mark">VERNA<br>TOUCH</div>
<p class="abs about-text">Lorem ipsum dolor sit amet, consectetur adipisicing elit, sed do eiusmod tempor incididunt ut labore et dolore magna aliqua. Ut enim ad minim veniam, quis nostrud exercitation ullamco laboris nisi ut aliquip ex ea commodo consequat. Duis aute irure dolor in reprehenderit in voluptate velit esse cillum dolore eu fugiat nulla pariatur. Excepteur sint occaecat cupidatat non proident, sunt in</p>

<ul class="abs f-links">
  <li>Passion</li><li>Education</li><li>Treatments</li><li>Advice</li><li>Packages</li><li>Testimonials</li>
</ul>

<div class="abs contact">
  <div class="contact-row"><svg viewBox="0 0 10 10"><path d="M5 0.5a3.2 3.2 0 0 0-3.2 3.2C1.8 6 5 9.5 5 9.5s3.2-3.5 3.2-5.8A3.2 3.2 0 0 0 5 0.5zm0 4.4a1.2 1.2 0 1 1 0-2.4 1.2 1.2 0 0 1 0 2.4z" fill="#15a9c9"/></svg>Space for the postal address of Verna Touch</div>
  <div class="contact-row"><svg viewBox="0 0 10 10"><path d="M2.2 0.8l1.6 1.9-.9 1.2c.6 1.3 1.6 2.3 2.9 2.9l1.2-.9 1.9 1.6-.9 1.5C4.6 8.9 1 5.4.8 1.7z" fill="#15a9c9"/></svg>206.555.0147</div>
  <div class="contact-row"><svg viewBox="0 0 10 10"><rect x="0.5" y="1.8" width="9" height="6.6" fill="#15a9c9"/><path d="M0.8 2.2 5 5.4 9.2 2.2" stroke="#2d2a74" stroke-width="0.9" fill="none"/></svg>vernatouchmassage@quillmail.test</div>
  <div class="contact-row"><svg viewBox="0 0 10 10"><circle cx="5" cy="5" r="4" stroke="#15a9c9" stroke-width="1.3" fill="none"/><path d="M5 2.6V5h1.8" stroke="#15a9c9" stroke-width="1.1" fill="none"/></svg>Mon - Sat: 9:00 - 18:00</div>
</div>

<div class="social" style="left:502px" aria-label="Social link 1"></div>
<div class="social" style="left:542px" aria-label="Social link 2"></div>
<div class="social" style="left:582px" aria-label="Social link 3"></div>
<div class="social" style="left:622px" aria-label="Social link 4"></div>
<div class="social" style="left:662px" aria-label="Social link 5"></div>

<div class="abs copyright">© 2015, Verna Touch Mobile Massage. All rights reserved.</div>

</body>
</html>
```